Business Card Design

I need a business card that is sleek/professional, I am a hair stylist that is trendy and I want my business cards to fit my style. I would like for them to be black or gray and maybe the print to be white. I also want them to be read easily, I don't want clients to have to squint their eyes to see the print. I want the back of the card to have a space for me to write there next appointment on and maybe a short sentence thanking them for their visit.

Industry/Entity Type

Hair

Contact Information for Business Card

Hair Horizons by Tavio @ Marcus Delane Salons, Owner/Hair Stylist/Makeup Artist-Tavio Ormonde ,Kelmar Method Educator, 4186F Meadow Crest Blvd Ste.302 Sugarland Tx 77512,Phone# 281-555-0246

```html
<!DOCTYPE html>
<html lang="en">
<head>
<meta charset="utf-8">
<title>Hair Stylist Business Card</title>
<link href="https://fonts.googleapis.com/css2?family=Fondamento:ital@0;1&family=Comic+Neue:wght@400&family=Libre+Baskerville&display=swap" rel="stylesheet">
<style>
  :root {
    --paper: #ffffff;
    --card: #000000;
    --ink: #ffffff;
  }
  * { margin: 0; padding: 0; box-sizing: border-box; }
  html, body { width: 1052px; height: 1200px; overflow: hidden; background: var(--paper); }
  .sheet { position: relative; width: 1052px; height: 1200px; }
  .card { position: absolute; background: var(--card); color: var(--ink); overflow: hidden; }
  .card--front { left: 18px; top: 10px; width: 1016px; height: 580px; }
  .card--back { left: 21px; top: 608px; width: 1010px; height: 578px; }
  .title {
    position: absolute; left: 26px; top: 22px;
    font-family: "Fondamento", cursive;
    font-size: 112px; line-height: 1; white-space: nowrap; letter-spacing: 1px;
  }
  .card--back .title { left: 24px; top: 16px; }
  .tagline {
    position: absolute; left: 672px; top: 160px;
    font-family: "Fondamento", cursive; font-style: italic;
    font-size: 33px; white-space: nowrap;
  }
  .card--back .tagline { left: 666px; top: 160px; }
  .title-rule { position: absolute; left: 0; top: 162px; width: 660px; height: 4px; background: var(--ink); }
  .hair-art {
    position: absolute; right: 0; bottom: 0; width: 400px; height: 360px;
    background: radial-gradient(ellipse at 65% 30%, #ffffff 0%, #f2f2f2 45%, #000000 80%);
    border-top-left-radius: 180px 140px;
  }
  .card--back .hair-art { height: 370px; }
  .contact {
    position: absolute; left: 12px; top: 450px;
    font-family: "Comic Neue", "Comic Sans MS", cursive;
    font-size: 21px; line-height: 29px; letter-spacing: 0.3px;
  }
  .next-visit {
    position: absolute; left: 14px; top: 240px;
    font-family: "Libre Baskerville", serif;
    font-size: 58px; line-height: 1;
  }
</style>
</head>
<body>
<main class="sheet">
  <section class="card card--front">
    <h1 class="title">Hair stylist</h1>
    <p class="tagline">thanks for ur visit</p>
    <div class="hair-art" role="img" aria-label="White silhouette of a styled hairdo"></div>
    <address class="contact" style="font-style: normal;">
      Hair Horizons by Tavio @ Marcus Delane Salons,<br>
      Owner/Hair Stylist/Makeup Artist-Tavio Ormonde ,Kelmar<br>
      Method Educator, 4186F Meadow Crest Blvd Ste.302<br>
      Sugarland Tx 77512,Phone# 281-555-0246
    </address>
  </section>
  <section class="card card--back">
    <h2 class="title">Hair stylist</h2>
    <div class="title-rule"></div>
    <p class="tagline">thanks for ur visit</p>
    <p class="next-visit">Next Visit Date</p>
    <div class="hair-art" role="img" aria-label="White silhouette of a styled hairdo"></div>
  </section>
</main>
</body>
</html>
```